Envelope Design - Winner can do follow-up business

- Varindo.com is a Swiss-based online store selling business shirts and accessories for business men
- Please visit the webpage to make yourself familiar with the company. Although the text is in German, with Google translator you should be able to understand the main content.
- Our clients are mainly business men between 30 and 60 years old. Mostly with a high income working in the service industry (banking, insurance, lawyers, etc.). Sometimes there wives purchase the shirts for them ;-)
- The colors and the logo are given, as they are also used for the print materials (please see files in attachment)
- I am running several businesses and often need a talented web designer --> the winner gets substantial follow-up business
your task:
-for our company we need a new envelope design
-It should be simple and modern
-please use one of the logos in the followings.
-suprise me :)

```html
<!DOCTYPE html>
<html lang="en">
<head>
<meta charset="utf-8">
<title>Varindo Envelope</title>
<link href="https://fonts.googleapis.com/css2?family=Josefin+Sans:wght@300;400&display=swap" rel="stylesheet">
<style>
  :root {
    --bg: #e9e9e9;
    --black: #0b0b0b;
    --paper: #ffffff;
    --gold: #e6c437;
    --red: #c61f1f;
    --window: #bdbdbd;
    --window-edge: #e2e2e2;
  }
  html, body {
    margin: 0;
    width: 1200px;
    height: 928px;
    overflow: hidden;
    background: var(--bg);
    font-family: "Josefin Sans", sans-serif;
  }
  .canvas {
    position: relative;
    width: 1200px;
    height: 928px;
  }
  .envelope {
    position: absolute;
    left: 220px;
    width: 760px;
    height: 380px;
    box-shadow: 0 6px 18px rgba(0,0,0,0.18);
    overflow: hidden;
  }
  .envelope-back { top: 50px; background: var(--paper); }
  .envelope-front { top: 490px; background: var(--black); }

  .back-art { position: absolute; inset: 0; }
  .back-flap, .back-band { fill: var(--black); }

  .back-wordmark {
    position: absolute;
    left: 0; right: 0;
    top: 212px;
    text-align: center;
    color: var(--gold);
    font-weight: 300;
    font-size: 20px;
    letter-spacing: 6px;
  }
  .sender-line {
    position: absolute;
    left: 0; right: 0;
    top: 296px;
    text-align: center;
    color: var(--gold);
    font-weight: 400;
    font-size: 11px;
    letter-spacing: 0.6px;
  }

  .front-wordmark {
    position: absolute;
    left: 50px;
    top: 52px;
    color: var(--gold);
    font-weight: 300;
    font-size: 30px;
    letter-spacing: 8px;
  }
  .address-window {
    position: absolute;
    left: 50px;
    top: 130px;
    width: 240px;
    height: 80px;
    border-radius: 14px;
    background: var(--window);
    border: 2px solid var(--window-edge);
  }
  .accent-line {
    position: absolute;
    left: 0;
    right: 0;
    height: 3px;
  }
  .accent-red { top: 318px; background: var(--red); }
  .accent-gold { top: 326px; background: var(--gold); }
</style>
</head>
<body>
<main class="canvas">

  <section class="envelope envelope-back" aria-label="Envelope back">
    <svg class="back-art" viewBox="0 0 760 380" width="760" height="380" aria-hidden="true">
      <path class="back-flap" d="M0 0 H760 V60 C620 110 470 170 380 200 C290 170 140 110 0 60 Z"/>
      <path class="back-band" d="M0 270 C250 262 510 262 760 270 V380 H0 Z"/>
    </svg>
    <div class="back-wordmark">VARINDO</div>
    <div class="sender-line">Varindo GmbH | Seestrasse 48 | 8800 Thalwil | T: +41 44 720 55 10 | E: hello@varindo.com</div>
  </section>

  <section class="envelope envelope-front" aria-label="Envelope front">
    <div class="front-wordmark">VARINDO</div>
    <div class="address-window"></div>
    <div class="accent-line accent-red"></div>
    <div class="accent-line accent-gold"></div>
  </section>

</main>
</body>
</html>
```